Medicaid and Nursing Home Planning Law Firm Needs Customizable Flyer

We need a flyer for The Delvecki Law Firm, P.C. that incorporates our logo, color scheme and existing collaterals (see uploads) and that can be easily updated. The flyer could advertise an upcoming speech/seminar/gathering, but the text should be customizable so that we can revise it later on using either MSWord or some other basic software.

Industry/Entity Type

Legal

Requirements
Must have
• Logo and contact information for business, including address, (315) 555-0142, email and website information
Nice to have
• Also should advertise our 2nd location: 418 Brantley Avenue, Suite 305, Watertown, NY 13688

```html
<!DOCTYPE html>
<html lang="en">
<head>
<meta charset="utf-8">
<title>The Delvecki Law Firm — Services Flyer</title>
<link rel="stylesheet" href="https://fonts.googleapis.com/css2?family=Arimo:wght@400;700&family=Raleway:wght@500;600;700&display=swap">
<style>
  :root {
    --backdrop: #333231;
    --paper: #ffffff;
    --orange: #f07d1a;
    --rule-gray: #6b6b6b;
    --text-gray: #5a5a5a;
    --white: #ffffff;
    --photo-light: #e9b27a;
    --photo-mid: #c9844a;
    --photo-dark: #8a4f24;
  }
  * { box-sizing: border-box; margin: 0; padding: 0; }
  html, body {
    width: 1200px; height: 1000px; overflow: hidden;
    background: var(--backdrop);
  }
  .flyer {
    position: absolute; left: 191px; top: 171px;
    width: 803px; height: 568px;
    background: var(--paper);
    box-shadow: 3px 4px 6px rgba(0,0,0,0.55);
    overflow: hidden;
  }
  .about { position: absolute; left: 34px; top: 20px; right: 20px; }
  .about__title {
    font-family: "Raleway", sans-serif; font-weight: 700;
    font-size: 21px; color: var(--orange); letter-spacing: 0.2px;
    margin-bottom: 6px;
  }
  .about__text {
    font-family: "Arimo", sans-serif; font-size: 16px;
    line-height: 25px; color: var(--text-gray); letter-spacing: 0.3px;
    white-space: nowrap;
  }
  .rule { position: absolute; left: 0; right: 0; height: 4px; background: var(--rule-gray); }
  .rule--top { top: 167px; }
  .rule--bottom { top: 432px; }
  .services {
    position: absolute; left: 0; right: 0; top: 174px; height: 256px;
    background: var(--orange);
  }
  .services__photo {
    position: absolute; top: 0; right: 0; width: 460px; height: 100%;
    background:
      radial-gradient(ellipse 70% 60% at 65% 30%, var(--photo-light) 0%, rgba(233,178,122,0) 70%),
      linear-gradient(90deg, var(--orange) 0%, var(--photo-mid) 35%, var(--photo-light) 65%, var(--photo-dark) 100%);
  }
  .services__content { position: absolute; left: 25px; top: 21px; }
  .services__title {
    font-family: "Raleway", sans-serif; font-weight: 600;
    font-size: 20px; color: var(--white); margin-bottom: 10px;
  }
  .services__list { list-style: none; }
  .services__item {
    font-family: "Raleway", sans-serif; font-weight: 600;
    font-size: 20px; line-height: 30.6px; color: var(--white);
    letter-spacing: 0.2px; padding-left: 21px; position: relative;
  }
  .services__item::before {
    content: ""; position: absolute; left: 2px; top: 11px;
    width: 9px; height: 9px; border-radius: 50%; background: var(--white);
  }
  .footer__brand {
    position: absolute; left: 64px; top: 455px; width: 187px; height: 86px;
    display: flex; align-items: center; justify-content: center;
    font-family: "Raleway", sans-serif; font-weight: 500;
    font-size: 14px; letter-spacing: 0.6px; color: var(--text-gray);
    text-transform: uppercase; white-space: nowrap;
  }
  .footer__contact {
    position: absolute; left: 364px; top: 446px; width: 420px;
    text-align: center; font-family: "Arimo", sans-serif;
  }
  .footer__cta { font-size: 17px; line-height: 22px; color: var(--text-gray); }
  .footer__web { font-size: 17px; line-height: 22px; color: var(--orange); margin-top: 4px; }
  .footer__web strong { font-weight: 700; }
  .footer__details { margin-top: 6px; font-size: 12px; line-height: 16px; color: var(--text-gray); }
  .footer__details strong { font-weight: 700; color: var(--orange); }
</style>
</head>
<body>
  <main class="flyer">
    <section class="about">
      <h2 class="about__title">ABOUT US</h2>
      <p class="about__text">The Delvecki Law Firm, P.c. Was Founded In 2015 To Focus Solely On Planning For<br>Residents Of Central And Northern New York With Needs In Elder Law/medicaid Planning,<br>Estate Planning, Trust &amp; Estate Administration / Litigation, And Guardianship/special<br>Needs Planning Areas.</p>
    </section>

    <div class="rule rule--top"></div>

    <section class="services">
      <div class="services__photo" role="img" aria-label="Close-up photo of a last will and testament document with a red pen"></div>
      <div class="services__content">
        <h2 class="services__title">SERVICES WE OFFER</h2>
        <ul class="services__list">
          <li class="services__item">Elder law</li>
          <li class="services__item">Medicaid planning</li>
          <li class="services__item">Estate planning</li>
          <li class="services__item">Trust &amp; estate administration</li>
          <li class="services__item">Trust &amp; estate litigation</li>
          <li class="services__item">Guardianship &amp; special needs planning areas</li>
        </ul>
      </div>
    </section>

    <div class="rule rule--bottom"></div>

    <div class="footer__brand">The Delvecki Law Firm</div>
    <div class="footer__contact">
      <p class="footer__cta">BOOK A FREE CONSULTATION NOW!!</p>
      <p class="footer__web">www.<strong>thedelveckilaw</strong>firm.com</p>
      <div class="footer__details">
        <p><strong>Main Office:</strong> 75 Corliss Street, Suite 110, Syracuse, NY 13202</p>
        <p><strong>Second Office:</strong> 418 Brantley Avenue, Suite 305, Watertown, NY 13688</p>
        <p>(315) 555-0142 &nbsp;|&nbsp; info@thedelveckilawfirm.com</p>
      </div>
    </div>
  </main>
</body>
</html>
```